We Need a New Feature/Price comparison Table For Our Site

Hello,
We offer a subscription website to our clients highlighting available Bio/Pharma assets by therapeutic area, investment case, etc... (We are an investment bank in NYC).
However we are missing some design, most notably a nice pricing table. You can see it as it exists today if you look at the first attachment (Pricingtable). You can also see this on www.quelidon.com if you click on the ad on the right. Also please browse the site so you can get a better 'feel' for it.
We want the pricing section to look much nicer, but we aren't graphic designers so we're really not sure what the best way to do this would be.
I attached some images of pricing tables from other sites that look really nice, but obviously if we copied them exactly, they wouldn't fit with our design. So please be as creative and free as possible in designing something new for us. You can use the same info as on the pricing table on our site (First attachment). But that's all that should stay the same :)
Thanks in advance,
Morton
Industry/Entity Type
Investment
Look and feel
Each slider illustrates characteristics of the customer's brand and the style your logo design should communicate.

```html
<!DOCTYPE html>
<html lang="en">
<head>
<meta charset="utf-8">
<title>Pricing Plans</title>
<link rel="stylesheet" href="https://fonts.googleapis.com/css2?family=Arimo:wght@400;700&family=Roboto+Condensed:wght@700&display=swap">
<style>
  :root{
    --page:#ffffff;
    --ink:#454545;
    --rule:#c9c9c9;
    --band-top:#474747;
    --band-bottom:#232323;
    --band-text:#f2f2f2;
    --panel-top:#f7f7f7;
    --panel-bottom:#dcdcdc;
    --free-top:#b3c95a;
    --free-bottom:#7f9b28;
    --free-price:#c3d645;
    --premium-top:#bfd2ea;
    --premium-bottom:#88a8d3;
    --premium-price:#7fa4d9;
    --corporate-top:#f3d0d2;
    --corporate-bottom:#dea2a6;
    --corporate-price:#eaa9b0;
  }
  *{box-sizing:border-box;margin:0;padding:0}
  html,body{width:780px;height:1200px;overflow:hidden;background:var(--page)}
  .canvas{position:relative;width:780px;height:1200px;overflow:hidden;background:var(--page);font-family:"Arimo",Arial,sans-serif}
  .plan{position:absolute;top:82px;width:231px;display:flex;flex-direction:column}
  .plan--free{left:13px}
  .plan--premium{left:271px}
  .plan--corporate{left:528px}

  .plan__tab{height:70px;margin:0 6px;border-radius:6px 6px 0 0;display:flex;align-items:center;justify-content:center;
    font-family:"Roboto Condensed",Arial,sans-serif;font-size:18px;color:#fff;text-transform:uppercase;letter-spacing:.3px;
    text-shadow:0 1px 1px rgba(0,0,0,.35);box-shadow:inset 0 1px 0 rgba(255,255,255,.5)}
  .plan--free .plan__tab{background:linear-gradient(var(--free-top),var(--free-bottom))}
  .plan--premium .plan__tab{background:linear-gradient(var(--premium-top),var(--premium-bottom))}
  .plan--corporate .plan__tab{background:linear-gradient(var(--corporate-top),var(--corporate-bottom))}

  .band{height:62px;display:flex;align-items:center;justify-content:center;background:linear-gradient(var(--band-top),var(--band-bottom));
    color:var(--band-text);font-weight:700;font-size:18px;text-transform:uppercase;letter-spacing:.2px;box-shadow:0 2px 3px rgba(0,0,0,.3)}
  .band--footer{height:61px}

  .features{margin:0 6px;background:linear-gradient(var(--panel-top),var(--panel-bottom));display:flex;flex-direction:column;padding:0 12px}
  .features__item{flex:1;display:flex;align-items:center;justify-content:center;text-align:center;font-weight:700;font-size:18px;
    line-height:17px;color:var(--ink);border-bottom:1px solid var(--rule)}
  .features__item:last-child{border-bottom:none}

  .plan--free .features--buy{height:153px}
  .plan--free .features--sell{height:58px}
  .plan--paid .features--buy{height:462px}
  .plan--paid .features--sell{height:270px;padding-top:10px}
  .plan--paid .features--sell .features__item{border-bottom:none}

  .price{position:relative;margin:0 6px;height:85px;background:linear-gradient(var(--panel-bottom),#d6d6d6);
    display:flex;align-items:center;justify-content:center;font-family:"Roboto Condensed",Arial,sans-serif;font-size:38px;
    text-shadow:0 1px 0 rgba(0,0,0,.25)}
  .plan--paid .price{height:82px}
  .plan--free .price{color:var(--free-price)}
  .plan--premium .price{color:var(--premium-price)}
  .plan--corporate .price{color:var(--corporate-price)}
  .price__notch{position:absolute;top:50%;width:26px;height:46px;margin-top:-23px}
  .price__notch--left{left:-8px}
  .price__notch--right{right:-8px}

  .button{height:32px;border-radius:3px;display:flex;align-items:center;justify-content:center;gap:12px;
    font-size:13px;color:#333;box-shadow:0 1px 2px rgba(0,0,0,.5)}
  .button--register{width:90px;background:linear-gradient(#fafafa,#d2d2d2);border:1px solid #999}
  .button--buy{width:96px;border:1px solid rgba(0,0,0,.4);font-size:12px;font-weight:700}
  .plan--premium .button--buy{background:linear-gradient(#9dbce8,#5d88c8)}
  .plan--corporate .button--buy{background:linear-gradient(#f4c3c7,#dc8e95)}
  .button__icon{width:16px;height:16px}
</style>
</head>
<body>
<main class="canvas">

  <section class="plan plan--free" aria-label="Free plan">
    <div class="plan__tab">Free</div>
    <div class="band">Buy Side Features</div>
    <ul class="features features--buy">
      <li class="features__item">1 seat</li>
      <li class="features__item">Access Over 1,800<br>Listings</li>
      <li class="features__item">View Profiles of Over<br>800 Companies</li>
    </ul>
    <div class="band">Sell Side Features</div>
    <ul class="features features--sell">
      <li class="features__item">Add 1 listing</li>
    </ul>
    <div class="price">
      <svg class="price__notch price__notch--left" viewBox="0 0 26 46"><path d="M0 0H18L26 23L18 46H0Z" fill="#2e2e2e"/><path d="M8 19L12 23L8 27Z" fill="#aaa"/></svg>
      FREE
      <svg class="price__notch price__notch--right" viewBox="0 0 26 46"><path d="M26 0H8L0 23L8 46H26Z" fill="#2e2e2e"/><path d="M18 19L14 23L18 27Z" fill="#aaa"/></svg>
    </div>
    <div class="band band--footer"><span class="button button--register">Register</span></div>
  </section>

  <section class="plan plan--paid plan--premium" aria-label="Premium plan">
    <div class="plan__tab">Premium</div>
    <div class="band">Buy Side Features</div>
    <ul class="features features--buy">
      <li class="features__item">1 seat</li>
      <li class="features__item">Access Over 1,800<br>Listings</li>
      <li class="features__item">View Profiles of Over<br>800 Companies</li>
      <li class="features__item">3 Undisclosed<br>Items/Calls per Month</li>
      <li class="features__item">Access of Lead<br>Contacts and<br>Messaging Capabilities</li>
      <li class="features__item">View Proprietary<br>Listings</li>
      <li class="features__item">Download<br>Non-Confidential<br>Documents</li>
      <li class="features__item">Export Results to<br>Excel or PDF</li>
    </ul>
    <div class="band">Sell Side Features</div>
    <ul class="features features--sell">
      <li class="features__item">Add up to<br>25 listings</li>
      <li class="features__item">Screen Buy-Side<br>Dealmakers</li>
      <li class="features__item">Receice Custom<br>Sell-Side Analytics<br>(In Development)</li>
      <li class="features__item">50% Off Pipeline<br>Insight Subscription</li>
    </ul>
    <div class="price">
      <svg class="price__notch price__notch--left" viewBox="0 0 26 46"><path d="M0 0H18L26 23L18 46H0Z" fill="#2e2e2e"/><path d="M8 19L12 23L8 27Z" fill="#aaa"/></svg>
      $799
      <svg class="price__notch price__notch--right" viewBox="0 0 26 46"><path d="M26 0H8L0 23L8 46H26Z" fill="#2e2e2e"/><path d="M18 19L14 23L18 27Z" fill="#aaa"/></svg>
    </div>
    <div class="band band--footer"><span class="button button--buy">BUY <svg class="button__icon" viewBox="0 0 16 16"><circle cx="8" cy="8" r="7" fill="rgba(255,255,255,.55)"/><path d="M6.5 5L10 8L6.5 11Z" fill="#555"/></svg></span></div>
  </section>

  <section class="plan plan--paid plan--corporate" aria-label="Corporate plan">
    <div class="plan__tab">Corporate</div>
    <div class="band">Buy Side Features</div>
    <ul class="features features--buy">
      <li class="features__item">3 seats</li>
      <li class="features__item">Access Over 1,800<br>Listings</li>
      <li class="features__item">View Profiles of Over<br>800 Companies</li>
      <li class="features__item">9 Undisclosed<br>Items/Calls per Month</li>
      <li class="features__item">Access of Lead<br>Contacts and<br>Messaging Capabilities</li>
      <li class="features__item">View Proprietary<br>Listings</li>
      <li class="features__item">Download<br>Non-Confidential<br>Documents</li>
      <li class="features__item">Export Results to<br>Excel or PDF</li>
    </ul>
    <div class="band">Sell Side Features</div>
    <ul class="features features--sell">
      <li class="features__item">Add up to<br>1000 listings</li>
      <li class="features__item">Screen Buy-Side<br>Dealmakers</li>
      <li class="features__item">Receice Custom<br>Sell-Side Analytics<br>(In Development)</li>
      <li class="features__item">50% Off Pipeline<br>Insight Subscription</li>
    </ul>
    <div class="price">
      <svg class="price__notch price__notch--left" viewBox="0 0 26 46"><path d="M0 0H18L26 23L18 46H0Z" fill="#2e2e2e"/><path d="M8 19L12 23L8 27Z" fill="#aaa"/></svg>
      $1999
      <svg class="price__notch price__notch--right" viewBox="0 0 26 46"><path d="M26 0H8L0 23L8 46H26Z" fill="#2e2e2e"/><path d="M18 19L14 23L18 27Z" fill="#aaa"/></svg>
    </div>
    <div class="band band--footer"><span class="button button--buy">BUY <svg class="button__icon" viewBox="0 0 16 16"><circle cx="8" cy="8" r="7" fill="rgba(255,255,255,.55)"/><path d="M6.5 5L10 8L6.5 11Z" fill="#555"/></svg></span></div>
  </section>

</main>
</body>
</html>
```